Brenmoss Building Company needs a flyer to catch attention

A flyer that can be displayed at several different stores detailing our skills, work produced, experience and contact details. Information can be extracted from our website www.brenmossbc.co.nz. The flyer should feel very green, with addition of pics of work completed as well as stock images of lush green plants, lawns, landscape or similar. Needs to be eye catching with just enough information to express our experience and commitment to high standards

Target Market(s)

Residential
Landscape Architects

Industry/Entity Type

Landscaping

Font styles to use
Serif

Colors
abd037

Requirements
Must have
• Our logo
Experience
Services offered including pictures
All information avail on our website www.brenmossbc.co.nz
Nice to have
• stock images of lush greenery like a garden after fresh rainfall
Should not have
• Nothing comes to mind

```html
<!DOCTYPE html>
<html lang="en">
<head>
<meta charset="utf-8">
<title>Brenmoss Building Company – Flyers</title>
<link href="https://fonts.googleapis.com/css2?family=Source+Sans+3:wght@400;600;700&family=Oswald:wght@600&display=swap" rel="stylesheet">
<style>
:root{
  --bg:#e6e7e6;
  --paper:#ffffff;
  --green:#abd037;
  --green-mid:#6cb33f;
  --green-dark:#1f8a3b;
  --green-deep:#146b2c;
  --ink:#3d3d3d;
  --grey:#555;
}
*{box-sizing:border-box;margin:0;padding:0}
html,body{width:1200px;height:800px;overflow:hidden;background:var(--bg)}
body{font-family:"Source Sans 3",Arial,sans-serif;color:var(--ink);position:relative}
.flyer{position:absolute;top:60px;width:480px;height:680px;background:var(--paper);overflow:hidden;box-shadow:0 6px 18px rgba(0,0,0,.18)}
.flyer--intro{left:80px}
.flyer--services{left:640px}
.flyer__art{position:absolute;inset:0;width:480px;height:680px}
.logo{position:absolute;left:12px;top:14px;display:flex;align-items:center;gap:8px}
.logo__mark{width:62px;height:62px;border-radius:50%;background:var(--green-dark);border:4px solid var(--green)}
.logo__name{color:var(--green-dark);font-weight:600;font-size:16px;line-height:17px}
.values{position:absolute;right:22px;top:62px;text-align:right;color:#fff;font-weight:700;font-size:19px;line-height:23px;text-shadow:0 1px 2px rgba(0,0,0,.25)}
.badge{position:absolute;left:338px;top:225px;width:116px;height:116px;border-radius:50%;background:var(--green-deep);border:4px solid #fff;box-shadow:0 0 0 3px var(--green-deep);color:#fff;text-align:center;font-family:"Oswald",Arial,sans-serif}
.badge__top,.badge__bottom{font-size:11px;letter-spacing:2px;display:block}
.badge__top{margin-top:18px}
.badge__years{display:block;font-size:24px;line-height:30px;background:#fff;color:var(--green-deep);margin:6px -6px}
.intro__heading{position:absolute;left:20px;right:20px;top:360px;text-align:center;color:var(--green-dark);font-weight:600;font-size:14.5px;line-height:17px}
.intro__body{position:absolute;left:24px;right:24px;top:404px;text-align:center;color:var(--grey);font-size:10.5px;line-height:14px}
.tagline{position:absolute;left:0;right:0;top:596px;text-align:center;color:var(--green-dark);font-size:10.5px}
.pill{position:absolute;top:627px;height:22px;padding:0 20px;border-radius:11px;background:var(--green-mid);border:2px solid #d6ea9c;color:#fff;font-weight:600;font-size:12px;line-height:18px;white-space:nowrap}
.flyer--intro .pill{left:120px}
.flyer--services .pill{left:120px}
.footer{position:absolute;left:18px;right:18px;top:656px;display:flex;align-items:center;color:#fff}
.footer__web{font-size:12px;flex:1}
.footer__call{font-size:12px;margin-right:10px}
.footer__phone{display:flex;align-items:center;gap:6px;font-weight:700;font-size:17px}
.services__heading{position:absolute;left:22px;top:355px;color:var(--green-dark);font-weight:600;font-size:15px;line-height:19px}
.services__list{position:absolute;left:22px;top:408px;width:450px;display:grid;grid-template-columns:148px 146px 160px;row-gap:7px;list-style:none}
.service{display:flex;align-items:center;gap:8px;font-size:12px;color:#222;height:27px;white-space:nowrap}
.service__icon{width:27px;height:27px;border-radius:50%;background:var(--green-mid);border:2px solid #cfe6a8;position:relative;flex:none}
.service__icon::after{content:"";position:absolute;left:7px;top:7px;width:9px;height:9px;border-radius:2px;background:#fff}
</style>
</head>
<body>

<section class="flyer flyer--intro">
  <svg class="flyer__art" viewBox="0 0 480 680" aria-hidden="false">
    <defs>
      <linearGradient id="houseGrad" x1="0" y1="0" x2="1" y2="1">
        <stop offset="0" stop-color="#7c6a55"/><stop offset=".45" stop-color="#b2a48c"/><stop offset=".75" stop-color="#4f7a35"/><stop offset="1" stop-color="#6f9a3f"/>
      </linearGradient>
      <linearGradient id="grassBand" x1="0" y1="0" x2="0" y2="1">
        <stop offset="0" stop-color="#9fd04a"/><stop offset="1" stop-color="#3d8f2c"/>
      </linearGradient>
      <radialGradient id="paveGrad"><stop offset="0" stop-color="#d9c9b0"/><stop offset="1" stop-color="#5f8a3a"/></radialGradient>
      <radialGradient id="lawnGrad"><stop offset="0" stop-color="#c9ec7a"/><stop offset="1" stop-color="#3f9a2f"/></radialGradient>
      <radialGradient id="sprinkGrad"><stop offset="0" stop-color="#e8f1dc"/><stop offset="1" stop-color="#5c9a38"/></radialGradient>
    </defs>
    <path role="img" aria-label="Photo of a landscaped house frontage with garden path" d="M0,95 C120,128 250,112 330,62 C380,32 440,28 480,30 L480,290 C400,312 300,342 150,330 C80,322 30,310 0,298 Z" fill="url(#houseGrad)"/>
    <path d="M255,112 C320,62 400,28 480,30 L480,150 C430,156 360,150 300,132 Z" fill="#abd037" opacity=".88"/>
    <path d="M0,300 C80,330 200,345 300,330 C380,318 440,300 480,290" fill="none" stroke="#abd037" stroke-width="4"/>
    <path d="M0,312 C90,342 210,352 310,338 C390,326 440,312 480,302" fill="none" stroke="#6cb33f" stroke-width="5"/>
    <path d="M0,322 C100,352 220,360 320,345" fill="none" stroke="#444" stroke-width="2"/>
    <g>
      <circle cx="105" cy="520" r="60" fill="#1f8a3b"/><circle cx="105" cy="520" r="52" fill="#fff"/>
      <circle role="img" aria-label="Photo of paving and a timber bench" cx="105" cy="520" r="48" fill="url(#paveGrad)"/>
      <circle cx="250" cy="518" r="67" fill="#1f8a3b"/><circle cx="250" cy="518" r="59" fill="#fff"/>
      <circle role="img" aria-label="Close-up photo of fresh green lawn" cx="250" cy="518" r="55" fill="url(#lawnGrad)"/>
      <circle cx="395" cy="520" r="60" fill="#1f8a3b"/><circle cx="395" cy="520" r="52" fill="#fff"/>
      <circle role="img" aria-label="Photo of a lawn sprinkler watering grass" cx="395" cy="520" r="48" fill="url(#sprinkGrad)"/>
    </g>
    <path role="img" aria-label="Lush grass border" d="M0,628 C60,615 120,630 200,620 C300,610 400,628 480,616 L480,680 L0,680 Z" fill="url(#grassBand)"/>
  </svg>
  <div class="logo"><span class="logo__mark"></span><span class="logo__name">Brenmoss<br>Building Company</span></div>
  <p class="values">HONESTY<br>TEAMWORK<br>KNOWLEDGE</p>
  <div class="badge"><span class="badge__top">EXPERIENCE</span><span class="badge__years">25 YEARS</span><span class="badge__bottom">EXPERIENCE</span></div>
  <h2 class="intro__heading">Brenmoss Building Company offers services to large or small residential and commercial projects.</h2>
  <p class="intro__body">Whether you have a blank canvas or are looking to rejuvenate your property we are able to advise and make the process easy and stress free. From paving, pergolas and decks to concrete or planting your dream garden we have the expertise to help.</p>
  <p class="tagline">Give us a call and let's chat about getting the best solution to your landscaping needs!</p>
  <span class="pill">LOCALLY OWNED AND OPERATED</span>
  <div class="footer">
    <span class="footer__web">www.brenmossbc.co.nz</span>
    <span class="footer__call">Call today for your FREE QUOTE</span>
    <span class="footer__phone"><svg width="18" height="18" viewBox="0 0 24 24"><circle cx="12" cy="12" r="10.5" fill="none" stroke="#fff" stroke-width="2"/><path d="M8 7c1-1 2 0 2.5 1l.5 1.5c.2.6-.5 1.2-.9 1.5.6 1.4 1.6 2.4 3 3 .3-.4.9-1.1 1.5-.9l1.5.5c1 .5 2 1.5 1 2.5-2 2-9-3-9.1-9.1z" fill="#fff"/></svg>021 555 0148</span>
  </div>
</section>

<section class="flyer flyer--services">
  <svg class="flyer__art" viewBox="0 0 480 680">
    <defs>
      <linearGradient id="parkGrad" x1="0" y1="0" x2="0" y2="1">
        <stop offset="0" stop-color="#8fa27a"/><stop offset=".4" stop-color="#c9b99a"/><stop offset=".6" stop-color="#5f9a33"/><stop offset="1" stop-color="#4c8a2a"/>
      </linearGradient>
      <linearGradient id="grassBand2" x1="0" y1="0" x2="0" y2="1">
        <stop offset="0" stop-color="#9fd04a"/><stop offset="1" stop-color="#3d8f2c"/>
      </linearGradient>
      <linearGradient id="fenceGrad" x1="0" y1="0" x2="1" y2="0"><stop offset="0" stop-color="#7a4a2c"/><stop offset="1" stop-color="#b57a4c"/></linearGradient>
      <linearGradient id="tileGrad" x1="0" y1="0" x2="1" y2="1"><stop offset="0" stop-color="#d8dcd6"/><stop offset="1" stop-color="#5e6a70"/></linearGradient>
      <linearGradient id="poolGrad" x1="0" y1="0" x2="0" y2="1"><stop offset="0" stop-color="#9fc7d4"/><stop offset="1" stop-color="#bfbdb2"/></linearGradient>
    </defs>
    <path role="img" aria-label="Photo of a landscaped lawn and paved courtyard in front of a house" d="M0,95 C120,128 250,112 330,62 C380,32 440,28 480,30 L480,300 C400,320 300,345 150,332 C80,325 30,312 0,300 Z" fill="url(#parkGrad)"/>
    <path d="M255,112 C320,62 400,28 480,30 L480,150 C430,156 360,150 300,132 Z" fill="#abd037" opacity=".88"/>
    <path d="M0,302 C80,332 200,345 300,332" fill="none" stroke="#abd037" stroke-width="4"/>
    <path d="M0,314 C90,344 210,352 300,340" fill="none" stroke="#6cb33f" stroke-width="5"/>
    <path d="M300,330 C380,318 440,305 480,300" fill="none" stroke="#6cb33f" stroke-width="5"/>
    <circle cx="320" cy="296" r="52" fill="#6cb33f"/><circle cx="320" cy="296" r="47" fill="#fff"/>
    <circle role="img" aria-label="Photo of a timber slat fence" cx="320" cy="296" r="44" fill="url(#fenceGrad)"/>
    <circle cx="415" cy="270" r="58" fill="#6cb33f"/><circle cx="415" cy="270" r="53" fill="#fff"/>
    <circle role="img" aria-label="Photo of a tiled patio with outdoor seating" cx="415" cy="270" r="50" fill="url(#tileGrad)"/>
    <circle cx="383" cy="350" r="47" fill="#6cb33f"/><circle cx="383" cy="350" r="42" fill="#fff"/>
    <circle role="img" aria-label="Photo of a pool surrounded by paving" cx="383" cy="350" r="39" fill="url(#poolGrad)"/>
    <path role="img" aria-label="Lush grass border" d="M0,628 C60,615 120,630 200,620 C300,610 400,628 480,616 L480,680 L0,680 Z" fill="url(#grassBand2)"/>
  </svg>
  <div class="logo"><span class="logo__mark"></span><span class="logo__name">Brenmoss<br>Building Company</span></div>
  <p class="values">HONESTY<br>TEAMWORK<br>KNOWLEDGE</p>
  <h2 class="services__heading">Spend time enjoying your landscape,<br>not working in it</h2>
  <ul class="services__list">
    <li class="service"><span class="service__icon"></span>PATIOS</li>
    <li class="service"><span class="service__icon"></span>FENCING</li>
    <li class="service"><span class="service__icon"></span>RETAINING WALLS</li>
    <li class="service"><span class="service__icon"></span>PAVING</li>
    <li class="service"><span class="service__icon"></span>BOARDWALKS</li>
    <li class="service"><span class="service__icon"></span>GARDENS &amp; LAWNS</li>
    <li class="service"><span class="service__icon"></span>CONCRETE</li>
    <li class="service"><span class="service__icon"></span>TIMBER</li>
    <li class="service"><span class="service__icon"></span>IRRIGATION</li>
    <li class="service"><span class="service__icon"></span>WATER FEATURES</li>
    <li class="service"><span class="service__icon"></span>PLANTER BOXES</li>
    <li class="service"><span class="service__icon"></span>PROJECT MANAGEMENT</li>
    <li class="service"><span class="service__icon"></span>DECKING</li>
    <li class="service"><span class="service__icon"></span>PERGOLAS</li>
    <li class="service"><span class="service__icon"></span>CONSULTATION</li>
  </ul>
  <p class="tagline">Give us a call and let's chat about getting the best solution to your landscaping needs!</p>
  <span class="pill">LOCALLY OWNED AND OPERATED</span>
  <div class="footer">
    <span class="footer__web">www.brenmossbc.co.nz</span>
    <span class="footer__call">Call today for your FREE QUOTE</span>
    <span class="footer__phone"><svg width="18" height="18" viewBox="0 0 24 24"><circle cx="12" cy="12" r="10.5" fill="none" stroke="#fff" stroke-width="2"/><path d="M8 7c1-1 2 0 2.5 1l.5 1.5c.2.6-.5 1.2-.9 1.5.6 1.4 1.6 2.4 3 3 .3-.4.9-1.1 1.5-.9l1.5.5c1 .5 2 1.5 1 2.5-2 2-9-3-9.1-9.1z" fill="#fff"/></svg>021 555 0148</span>
  </div>
</section>

</body>
</html>
```